Business Card, Stationary, Fax Cover, and Email Signature
Telvar Capital
Professional
Derek Hollow
President/Founder
418 Bramble Creek Lane, Suite 327
Marlow Ridge, VA 20999
dhollow@telvarcapital.example
www.TelvarCapital.example
Credit Repair - Credit Restoration - Credit Education ( Centered Top)
Legally And Ethically Remove Derogatory Items From Your Credit Report (Bullet Point)
Help Establish New Positive Trade Lines
(Bullet Point)
Learn How To Maintain And Increase Your Credit Score (Bullet Point)
www.TelvarCapital.example (Centered Bottom)

```html
<!DOCTYPE html>
<html lang="en">
<head>
<meta charset="utf-8">
<title>Telvar Capital – Business Card</title>
<link href="https://fonts.googleapis.com/css2?family=Open+Sans:wght@400;600;700&display=swap" rel="stylesheet">
<style>
  :root {
    --backdrop: #5e6267;
    --card-white: #ffffff;
    --card-top-shade: #f1f2f4;
    --divider-grey: #c9ccd1;
    --blue-light: #2a6fc0;
    --blue-deep: #0d3d8c;
    --navy: #1a3f7a;
    --mark-blue: #1e7fd0;
    --text-light: #ffffff;
    --text-soft: #dfe8f6;
  }
  * { margin: 0; padding: 0; box-sizing: border-box; }
  html, body { width: 1200px; height: 780px; overflow: hidden; }
  body {
    background: var(--backdrop);
    font-family: "Open Sans", Arial, sans-serif;
    display: flex;
    align-items: center;
    justify-content: center;
  }
  .business-card {
    position: relative;
    width: 1000px;
    height: 572px;
    border-radius: 26px;
    overflow: hidden;
    background: linear-gradient(180deg, var(--card-white) 0%, var(--card-top-shade) 100%);
    box-shadow: 0 14px 30px rgba(0,0,0,0.35);
  }
  .brand-area {
    position: absolute;
    top: 0; left: 0; right: 0;
    height: 322px;
    display: flex;
    align-items: center;
    justify-content: center;
    gap: 24px;
  }
  .brand-dot {
    width: 112px; height: 112px;
    border-radius: 50%;
    background: var(--mark-blue);
  }
  .brand-name {
    font-weight: 400;
    font-size: 60px;
    letter-spacing: 1px;
    color: var(--navy);
    text-transform: uppercase;
  }
  .contact-band {
    position: absolute;
    left: 0; right: 0; bottom: 0;
    height: 250px;
    border-top: 10px solid var(--divider-grey);
    background: linear-gradient(180deg, var(--blue-light) 0%, var(--blue-deep) 100%);
    color: var(--text-light);
    display: flex;
  }
  .person {
    width: 508px;
    padding: 44px 30px 0 0;
    text-align: right;
  }
  .person-name { font-weight: 700; font-size: 28px; line-height: 1.2; }
  .person-title { font-size: 21px; color: var(--text-soft); margin-top: 4px; }
  .person-address { font-size: 20px; color: var(--text-soft); line-height: 1.35; margin-top: 6px; }
  .band-divider {
    width: 2px;
    margin: 36px 0;
    background: rgba(255,255,255,0.55);
  }
  .contact-list {
    list-style: none;
    padding: 32px 0 0 26px;
    font-size: 19px;
    line-height: 34px;
  }
  .contact-list li { display: flex; align-items: center; gap: 14px; white-space: nowrap; }
  .contact-icon { width: 20px; height: 20px; flex: none; }
</style>
</head>
<body>
  <div class="business-card">
    <div class="brand-area">
      <div class="brand-dot"></div>
      <div class="brand-name">Telvar Capital</div>
    </div>
    <div class="contact-band">
      <div class="person">
        <div class="person-name">Derek Hollow</div>
        <div class="person-title">President/Founder</div>
        <div class="person-address">418 Bramble Creek Lane<br>Suite 327<br>Marlow Ridge, VA 20999</div>
      </div>
      <div class="band-divider"></div>
      <ul class="contact-list">
        <li>
          <svg class="contact-icon" viewBox="0 0 20 20"><path fill="#fff" d="M5 2l3 4-2 2c1 2.5 3.5 5 6 6l2-2 4 3-2 3C9 18 2 11 2 4z"/></svg>
          (877) 555-0142(T)
        </li>
        <li>
          <svg class="contact-icon" viewBox="0 0 20 20"><path fill="#fff" d="M5 2l3 4-2 2c1 2.5 3.5 5 6 6l2-2 4 3-2 3C9 18 2 11 2 4z"/></svg>
          (703) 555-0186
        </li>
        <li>
          <svg class="contact-icon" viewBox="0 0 20 20"><rect x="5" y="2" width="10" height="6" fill="#fff"/><rect x="2" y="8" width="16" height="8" rx="1.5" fill="#fff"/><rect x="5" y="12" width="10" height="6" fill="#fff" stroke="#1b4f9e" stroke-width="1"/></svg>
          (703) 555-0193
        </li>
        <li>
          <svg class="contact-icon" viewBox="0 0 20 20"><rect x="1.5" y="4" width="17" height="12" rx="1.5" fill="#fff"/><path d="M2 5l8 6 8-6" fill="none" stroke="#1b4f9e" stroke-width="1.4"/></svg>
          dhollow@telvarcapital.example
        </li>
        <li>
          <svg class="contact-icon" viewBox="0 0 20 20"><circle cx="10" cy="10" r="8" fill="none" stroke="#fff" stroke-width="1.6"/><ellipse cx="10" cy="10" rx="3.5" ry="8" fill="none" stroke="#fff" stroke-width="1.4"/><path d="M2 10h16" stroke="#fff" stroke-width="1.4"/></svg>
          www.TelvarCapital.example
        </li>
      </ul>
    </div>
  </div>
</body>
</html>
```